Help designing a web admin portal for cloud access control company

Hello, we need help to design our web admin portal for our cloud based access control product called havenpost locks. Please see the attached admin portal wireframe. this is not absolute so we are open to UX / UI suggestions. This web admin portal will allow a admin at a small to medium sized business add new employees to their access control system and grant different access.
Updates

Project Deadline Extended
Reason: Waiting in a couple designs for people that said they would send something in

Target Market(s)

B2B

Industry/Entity Type

It Company

Font styles to use
Sans Serif

Colors
3277b5

Requirements
Must have
• Very simple and clean design. we like clean fonts like Oswald extra light. Please see an image of the wining app designs to see what the color and styling should look like

```html
<!DOCTYPE html>
<html lang="en">
<head>
<meta charset="utf-8">
<title>Havenpost Locks – Cameras</title>
<link rel="stylesheet" href="https://fonts.googleapis.com/css2?family=Oswald:wght@300;400&display=swap">
<style>
  :root {
    --page: #ffffff;
    --bar-dark: #333333;
    --bar-mid: #555555;
    --bar-strip: #666666;
    --tab: #7d7d7d;
    --door-box: #8a8a8a;
    --accent: #3277b5;
    --accent-soft: #55a2d6;
    --title-blue: #4e9ed4;
    --rule-blue: #9ccbea;
    --text-light: #ffffff;
    --feed-bg: #000000;
    --feed-frame: #9a9a9a;
  }
  * { box-sizing: border-box; margin: 0; padding: 0; }
  html, body { width: 1200px; height: 1000px; overflow: hidden; background: var(--page); }
  body { position: relative; font-family: "Oswald", "Arial Narrow", sans-serif; font-weight: 300; color: var(--text-light); }

  .topbar { position: absolute; left: 0; top: 74px; width: 1200px; height: 72px; background: var(--bar-dark); }
  .brand { position: absolute; left: 34px; top: 20px; display: flex; align-items: center; gap: 4px; }
  .brand-dot { width: 32px; height: 32px; border-radius: 50%; background: var(--accent-soft); }
  .brand-name { font-size: 20px; font-weight: 300; color: var(--text-light); }
  .welcome { position: absolute; right: 38px; top: 24px; font-size: 17px; }

  .sidebar { position: absolute; left: 0; top: 146px; width: 225px; height: 774px; background: var(--bar-dark); }
  .menu-toggle { position: absolute; left: 35px; top: 17px; }
  .nav { list-style: none; position: absolute; top: 76px; left: 0; width: 225px; }
  .nav li { height: 42.5px; line-height: 40px; padding-left: 35px; font-size: 17px; text-transform: uppercase; }
  .nav li.is-active { background: var(--accent-soft); }
  .date { position: absolute; left: 28px; bottom: 22px; font-size: 14px; text-decoration: underline; }

  .door-bar { position: absolute; left: 225px; top: 146px; width: 975px; height: 50px; background: var(--bar-mid); }
  .door-strip { position: absolute; left: 333px; top: 0; width: 470px; height: 50px; background: var(--bar-strip); }
  .door-tab { position: absolute; left: 155px; top: 0; width: 178px; height: 50px; background: var(--tab); font-size: 17px; line-height: 48px; padding-left: 22px; }
  .door-tab-arrow { position: absolute; left: 333px; top: 10px; }
  .door { position: absolute; top: 8px; display: flex; align-items: center; gap: 6px; }
  .door-label { font-size: 11.5px; line-height: 14px; }
  .door-switch { width: 44px; height: 30px; background: var(--door-box); }
  .door-switch.is-selected { border: 2px solid var(--accent-soft); }

  .content-title { position: absolute; left: 353px; top: 233px; font-size: 26px; color: var(--title-blue); }
  .content-rule { position: absolute; left: 353px; top: 271px; width: 661px; height: 1px; background: var(--rule-blue); }

  .feed { position: absolute; width: 329px; background: var(--feed-bg); border: 1px solid var(--feed-frame); border-bottom: none; }
  .feed-label { position: absolute; left: 20px; bottom: 10px; font-size: 14px; }
  .feed-view { position: absolute; left: 0; width: 100%; }
  .feed-view.entrance { top: 23px; height: 190px; background: linear-gradient(180deg, #6d757c 0%, #8a8c88 40%, #4d4640 100%); }
  .feed-view.meeting { top: 0; height: 250px; background: linear-gradient(180deg, #4a4e4a 0%, #3a3d3a 55%, #2b2d2c 100%); }
</style>
</head>
<body>
  <header class="topbar">
    <div class="brand"><span class="brand-dot"></span><span class="brand-name">Havenpost Locks</span></div>
    <div class="welcome">Welcome, Marcus!</div>
  </header>

  <nav class="sidebar">
    <svg class="menu-toggle" width="27" height="16" viewBox="0 0 27 16" aria-hidden="true">
      <g stroke="#ffffff" stroke-width="1.6"><line x1="0" y1="1" x2="27" y2="1"/><line x1="0" y1="8" x2="27" y2="8"/><line x1="0" y1="15" x2="27" y2="15"/></g>
    </svg>
    <ul class="nav">
      <li>Home</li><li>Dashboard</li><li>Controller</li><li>Doors</li><li>Employees</li>
      <li>Open/ Close Times</li><li class="is-active">Cameras</li><li>Time Cards</li><li>Reports</li><li>Settings</li>
    </ul>
    <div class="date">SUNDAY, 11 / 27 / 16</div>
  </nav>

  <div class="door-bar">
    <div class="door-strip"></div>
    <div class="door-tab">Manual Door Opening</div>
    <svg class="door-tab-arrow" width="16" height="30" viewBox="0 0 16 30" aria-hidden="true"><polygon points="0,0 15,15 0,30" fill="#7d7d7d"/></svg>
    <div class="door" style="left:376px"><span class="door-label">Main<br>Door</span><span class="door-switch is-selected"></span></div>
    <div class="door" style="left:477px"><span class="door-label">Back<br>Door</span><span class="door-switch"></span></div>
    <div class="door" style="left:576px"><span class="door-label">Exec<br>Office</span><span class="door-switch"></span></div>
    <div class="door" style="left:679px"><span class="door-label">Storage<br>Room</span><span class="door-switch"></span></div>
  </div>

  <h1 class="content-title">Cameras</h1>
  <div class="content-rule"></div>

  <section class="feed" style="left:355px;top:295px;height:277px">
    <div class="feed-view entrance" role="img" aria-label="Live camera view of a person walking through the entrance"></div>
    <span class="feed-label">CAM 1 - [ Entrance]</span>
  </section>
  <section class="feed" style="left:685px;top:295px;height:277px">
    <span class="feed-label">CAM 2 - [ Camera Location ]</span>
  </section>
  <section class="feed" style="left:355px;top:581px;height:291px">
    <span class="feed-label">CAM 3- [ Camera Location ]</span>
  </section>
  <section class="feed" style="left:685px;top:581px;height:291px">
    <div class="feed-view meeting" role="img" aria-label="Live camera view of a meeting room with two people at a table"></div>
    <span class="feed-label">CAM 4 - [ Camera Location ]</span>
  </section>
</body>
</html>
```